Coffee pack for specialty coffee roasters

Tres Lunas is a premium brand of specialty coffee roasters based in Prague in the Czech Republic.
We sell coffee beans to other coffee shops (wholesale channel) or to final consumers in our own coffee shops (retail)
We are roasting only specialty grade coffee that we source either directly or through specialty coffee merchants.
We have usually 6-8 coffees on our offer list. Each coffee stays with us 2-7 months based on their harvest season.
We pack our coffee for retail purposes in 250g bags that we sell in our cafés, roastery and clients.
We are now changing our bags from side gusset bags with valve closed by tin ties to flat bottom bags with zipper and valve.
We want evolution of our packaging design (not revolution)
Our current bags are decorated by front and back stickers.
New bags will be custom printed with general information and logo (e.g. Manufacturer information, contact, size etc.) and we want to have paper sleeve with customizable information (e.g. Name of the Coffee origin, farmer, taste profile, farm info etc.)

Target Market(s)

Men + woman aged 25-45, socioeconomical group A and B, university educated, interested in quality products, they care about what they drink and eat.

Industry/Entity Type

Coffee Shop

Font styles to use
Other font styles liked:
• Platform regular

Requirements
Must have
• Design of the pack itself and design of paper sleeve that will be excheangable (we need to change name of the coffee and information about it on the paper sleeve)
Nice to have
• nice to have- coffee related design on the bag under the sleeve
Should not have
• any crazy colours (the bag is golden with only black print on it) and sleeve can be colourful but nothing extravagant.

```html
<!DOCTYPE html>
<html lang="cs">
<head>
<meta charset="utf-8">
<title>Tres Lunas – coffee bag and sleeve</title>
<link href="https://fonts.googleapis.com/css2?family=Jost:wght@400;500&family=Red+Hat+Display:wght@400;500&display=swap" rel="stylesheet">
<style>
  :root {
    --bg: #e9e4da;
    --gold: #d6bd77;
    --gold-shade: #c9ae66;
    --ink: #231f20;
    --sleeve: #231f20;
    --sleeve-type: #f7d98a;
    --map-tone: #f2f0ea;
  }
  * { margin: 0; padding: 0; box-sizing: border-box; }
  html, body { width: 1200px; height: 1200px; overflow: hidden; background: var(--bg); }
  .canvas { position: relative; width: 1200px; height: 1200px; font-family: "Jost", sans-serif; color: var(--ink); }

  .bag { position: absolute; background: var(--gold); border-radius: 14px 14px 2px 2px; overflow: hidden; }
  .bag--back { left: 76px; top: 232px; width: 448px; height: 680px; }
  .bag--front { left: 700px; top: 224px; width: 452px; height: 680px; }

  .zipper { position: absolute; left: 0; right: 0; top: 78px; height: 38px;
    border-top: 1px dashed rgba(35,31,32,.45); border-bottom: 1px dashed rgba(35,31,32,.45); }
  .zipper::after { content: ""; position: absolute; left: 0; right: 0; top: 18px; border-top: 1px dashed rgba(35,31,32,.45); }
  .zipper-label { position: absolute; left: 50%; top: 2px; transform: translateX(-50%);
    background: var(--gold); padding: 0 4px; font-size: 26px; color: rgba(35,31,32,.5); letter-spacing: -.5px; line-height: 30px; }

  .illustration { position: absolute; left: 130px; top: 128px; width: 180px; height: 140px;
    background: radial-gradient(ellipse at center, var(--gold-shade) 0%, var(--gold) 75%); border-radius: 50%; }

  .rule { position: absolute; left: 40px; right: 40px; top: 270px; border-top: 2px solid var(--ink); }
  .intro { position: absolute; left: 40px; right: 40px; top: 280px; font-size: 12.4px; line-height: 17px;
    text-align: justify; text-align-last: left; }
  .weight { position: absolute; left: 0; right: 0; bottom: 14px; text-align: center; font-size: 15px; }

  .sleeve { position: absolute; background: var(--sleeve); color: var(--sleeve-type); overflow: hidden; }
  .sleeve--back { left: 70px; top: 570px; width: 458px; height: 292px; }
  .sleeve--front { left: 688px; top: 576px; width: 470px; height: 302px; }

  .variety { position: absolute; left: 12px; top: 52px; font-size: 51px; line-height: 1; letter-spacing: -1.5px; white-space: nowrap; }
  .origin { position: absolute; left: 12px; top: 112px; font-size: 66px; line-height: 1; letter-spacing: -2px; }
  .process { position: absolute; left: 274px; top: 148px; font-size: 18px; white-space: nowrap; }
  .roast-date { position: absolute; left: 108px; top: 258px; display: flex; align-items: center; gap: 4px; font-size: 14px; }
  .roast-date .label { margin-right: 2px; }
  .roast-date .box { width: 22px; height: 18px; background: var(--sleeve-type); color: var(--gold-shade); font-size: 12px; text-align: center; line-height: 18px; }
  .roast-date .gap { width: 8px; }

  .brand { position: absolute; left: 0; right: 0; top: 190px; display: flex; flex-direction: column; align-items: center; gap: 22px; }
  .brand-dot { width: 80px; height: 80px; border: 6px solid var(--ink); border-radius: 50%; }
  .brand-name { font-size: 38px; font-weight: 500; letter-spacing: .5px; }

  .country { position: absolute; left: 32px; top: 88px; font-size: 66px; line-height: 1; letter-spacing: -1px; white-space: nowrap; }
  .facts { position: absolute; left: 120px; top: 170px; font-family: "Red Hat Display", sans-serif; font-size: 15px; line-height: 18.5px; color: #fff; letter-spacing: 1.2px; }
  .facts .facts-country { color: var(--sleeve-type); }
  .map { position: absolute; left: 326px; top: 0; width: 144px; height: 302px;
    background: linear-gradient(180deg, rgba(242,240,234,.9) 0%, rgba(242,240,234,.55) 100%); }
  .map-pin { position: absolute; left: 332px; top: 143px; width: 14px; height: 14px; border: 2px solid var(--sleeve-type); border-radius: 50%; background: var(--sleeve); }
</style>
</head>
<body>
<main class="canvas">
  <section class="bag bag--back" aria-label="Zadní strana sáčku">
    <div class="zipper"><span class="zipper-label">ZIPPER</span></div>
    <div class="illustration" role="img" aria-label="Kresba větvičky kávovníku s plody a listy"></div>
    <div class="rule"></div>
    <p class="intro">V ruce držíte čerstvě praženou zrnkovou kávu. Pracujeme výhradně s výběrovými jednodruhovými arabikami, které získali 85+ bodů. Káva se sbírá na farmách ručně a my navazujeme, co nejčerstvější úrodu přímo z farmy. Tato</p>
    <p class="weight">Hmotnost: 250g</p>
  </section>

  <section class="sleeve sleeve--back" aria-label="Přebal – Pichincha">
    <p class="variety">100% arabica caturra</p>
    <p class="origin">Pichincha</p>
    <p class="process">zpracování: promyté</p>
    <div class="roast-date">
      <span class="label">Praženo:</span>
      <span class="box">D</span><span class="box">D</span><span class="gap"></span>
      <span class="box">M</span><span class="box">M</span><span class="gap"></span>
      <span class="box">Y</span><span class="box">Y</span>
    </div>
  </section>

  <section class="bag bag--front" aria-label="Přední strana sáčku">
    <div class="brand">
      <span class="brand-dot"></span>
      <span class="brand-name">TRES LUNAS</span>
    </div>
  </section>

  <section class="sleeve sleeve--front" aria-label="Přebal – Ekvádor">
    <div class="map" role="img" aria-label="Mapa Střední a Jižní Ameriky s vyznačeným Ekvádorem"></div>
    <span class="map-pin"></span>
    <p class="country">EKVÁDOR</p>
    <p class="facts">
      <span class="facts-country">ECUADOR</span><br>
      100% arabica caturra<br>
      zpracování: promyté<br>
      farma: La Quinta Verde<br>
      Lískové ořechy
    </p>
  </section>
</main>
</body>
</html>
```